Crumble Cove Supper Invitation

We will be having a Fish Fry on May 17th from 6PM -10PM. Location is 4721 Larkspur Ln. Mansfield, TX 76058. We need a Invitation, which includes a the header reading "Crumble Cove Supper". Wording of "Crumble Cove Supper" should incorporate both baseball and food batter. Think baseball bats dripping in batter. Admission to all you can eat fish fry will be a donation of any baseball equipment including: bats, gloves, jerseys, cleats, balls, or financial donation. Proceeds will go towards funding Pemberly Family in traveling to Dominican Republic to conduct baseball ministries. It would great to incorporate Dominican Republic flag or colors.

```html
<!DOCTYPE html>
<html lang="en">
<head>
<meta charset="utf-8">
<title>Crumble Cove Supper Invitation</title>
<link rel="stylesheet" href="https://fonts.googleapis.com/css2?family=Bebas+Neue&family=Roboto:wght@400;700&display=swap">
<style>
  :root {
    --backdrop: #808285;
    --navy: #1b3160;
    --red: #ed1c24;
    --white: #ffffff;
    --gold: #e39a3c;
    --crumb: #f3c26e;
  }
  html, body {
    margin: 0;
    padding: 0;
    width: 965px;
    height: 1200px;
    overflow: hidden;
    background: var(--backdrop);
  }
  .invitation {
    position: absolute;
    left: 82px;
    top: 82px;
    width: 800px;
    height: 1035px;
    display: block;
    background: var(--white);
  }
  .display { font-family: "Bebas Neue", "Arial Narrow", sans-serif; }
  .body-text { font-family: "Roboto", Arial, sans-serif; }
  .fill-navy { fill: var(--navy); }
  .fill-red { fill: var(--red); }
  .fill-white { fill: var(--white); }
  .event-emblem-name { font-family: "Bebas Neue", "Arial Narrow", sans-serif; fill: var(--navy); }
  .date-label { font-weight: 400; fill: var(--navy); }
  .date-value { font-weight: 700; fill: var(--red); }
  .address { font-weight: 400; fill: var(--navy); }
</style>
</head>
<body>
<svg class="invitation" viewBox="0 0 1275 1650" xmlns="http://www.w3.org/2000/svg">
  <defs>
    <linearGradient id="fishPhotoTone" x1="0" y1="0" x2="1" y2="1">
      <stop offset="0" stop-color="#d98a35"/>
      <stop offset="0.45" stop-color="#f0b45a"/>
      <stop offset="0.7" stop-color="#f4e9dc"/>
      <stop offset="1" stop-color="#e6a14a"/>
    </linearGradient>
  </defs>

  <rect class="fill-white" x="0" y="0" width="1275" height="1650"/>

  <!-- Hero food photo area -->
  <polygon class="hero-photo" role="img" aria-label="Close-up photo of crispy golden fried fish fillets with a dollop of white tartar sauce"
           points="0,0 1275,0 1275,600 638,760 0,600" fill="url(#fishPhotoTone)"/>

  <!-- Ribbon bands -->
  <polygon class="band-left fill-navy" points="0,624 638,800 638,880 0,690"/>
  <polygon class="band-right fill-navy" points="1275,624 1275,690 638,880 638,800"/>
  <polygon class="wedge-left fill-navy" points="0,709 250,774 0,820"/>
  <polygon class="wedge-right fill-red" points="1275,709 1275,860 1030,774"/>

  <!-- Fish illustrations -->
  <ellipse class="fish-art fill-red" role="img" aria-label="Red tuna fish illustration facing right" cx="205" cy="870" rx="175" ry="55"/>
  <ellipse class="fish-art fill-navy" role="img" aria-label="Navy tuna fish illustration facing left" cx="1070" cy="870" rx="175" ry="55"/>

  <!-- Event emblem -->
  <g class="event-emblem">
    <rect class="fill-white" x="470" y="700" width="336" height="170"/>
    <text class="event-emblem-name" x="638" y="775" text-anchor="middle" font-size="68" textLength="290" lengthAdjust="spacingAndGlyphs">CRUMBLE COVE</text>
    <text class="event-emblem-name" x="638" y="845" text-anchor="middle" font-size="68">SUPPER</text>
  </g>

  <!-- Headline -->
  <text class="headline display fill-navy" x="638" y="1099" text-anchor="middle" font-size="196" textLength="1150" lengthAdjust="spacingAndGlyphs">CRUMBLE COVE SUPPER</text>
  <text class="subhead display fill-red" x="638" y="1184" text-anchor="middle" font-size="86" textLength="1145" lengthAdjust="spacingAndGlyphs">WITH BASEBALL BATS DRIPPING IN FISH BATTER</text>

  <!-- Admission bar -->
  <g class="admission">
    <polygon class="fill-navy" points="45,1317 95,1204 505,1204 455,1317"/>
    <polygon class="fill-red" points="450,1306 490,1217 1215,1217 1175,1306"/>
    <text class="display fill-white" x="103" y="1295" font-size="100" textLength="337" lengthAdjust="spacingAndGlyphs">ADMISSION:</text>
    <text class="display fill-white" x="493" y="1293" font-size="90" textLength="672" lengthAdjust="spacingAndGlyphs">ALL-YOU-CAN-EAT FISH FRY</text>
  </g>

  <!-- Donation band -->
  <rect class="donation-band fill-red" x="0" y="1377" width="1275" height="113"/>
  <polygon class="entry-tab fill-navy" points="214,1404 249,1347 1064,1347 1024,1404"/>
  <text class="display fill-white" x="638" y="1390" text-anchor="middle" font-size="54" textLength="755" lengthAdjust="spacingAndGlyphs">ENTRY IS A DONATION OF ANY BASEBALL EQUIPMENT</text>

  <g class="donation-items display fill-white" font-size="64">
    <text x="31" y="1468" textLength="85" lengthAdjust="spacingAndGlyphs">BATS</text>
    <text x="149" y="1468" textLength="131" lengthAdjust="spacingAndGlyphs">GLOVES</text>
    <text x="314" y="1468" textLength="146" lengthAdjust="spacingAndGlyphs">JERSEYS</text>
    <text x="494" y="1468" textLength="124" lengthAdjust="spacingAndGlyphs">CLEATS</text>
    <text x="652" y="1468" textLength="106" lengthAdjust="spacingAndGlyphs">BALLS</text>
    <text x="792" y="1468" textLength="452" lengthAdjust="spacingAndGlyphs">FINANCIAL CONTRIBUTION</text>
  </g>
  <g class="item-dividers fill-navy">
    <rect x="130" y="1420" width="4" height="55"/>
    <rect x="295" y="1420" width="4" height="55"/>
    <rect x="476" y="1420" width="4" height="55"/>
    <rect x="634" y="1420" width="4" height="55"/>
    <rect x="774" y="1420" width="4" height="55"/>
  </g>

  <!-- Dominican flag blocks -->
  <g class="flag flag-left">
    <rect class="fill-navy" x="30" y="1517" width="59" height="40"/>
    <rect class="fill-red" x="113" y="1517" width="59" height="40"/>
    <rect class="fill-red" x="30" y="1583" width="59" height="42"/>
    <rect class="fill-navy" x="113" y="1583" width="59" height="42"/>
  </g>
  <g class="flag flag-right">
    <rect class="fill-navy" x="1103" y="1517" width="59" height="40"/>
    <rect class="fill-red" x="1186" y="1517" width="59" height="40"/>
    <rect class="fill-red" x="1103" y="1583" width="59" height="42"/>
    <rect class="fill-navy" x="1186" y="1583" width="59" height="42"/>
  </g>

  <!-- Event details -->
  <text class="event-date body-text" x="195" y="1562" font-size="50" textLength="885" lengthAdjust="spacingAndGlyphs"><tspan class="date-label">Date &amp; Time: </tspan><tspan class="date-value">May 17th, 6 PM – 10 PM</tspan></text>

  <g class="pin-icon fill-red">
    <path d="M219,1580 a14,14 0 0 1 14,14 c0,10 -14,22 -14,22 c0,0 -14,-12 -14,-22 a14,14 0 0 1 14,-14 z M219,1588 a6,6 0 1 0 0.01,0 z" fill-rule="evenodd"/>
    <rect x="198" y="1618" width="44" height="7"/>
  </g>
  <text class="address body-text" x="260" y="1620" font-size="50" textLength="820" lengthAdjust="spacingAndGlyphs">4721 Larkspur Ln. Mansfield, TX 76058</text>
</svg>
</body>
</html>
```